Cleaning Company Banner

Looking to have a Banner made that shows our contact information and shows what we do with good imagery to catch cars driving by. Will be a 6' x 3' banner (landscape). Attached our logo and flyer that we currently hand out.

```html
<!DOCTYPE html>
<html lang="en">
<head>
<meta charset="UTF-8">
<title>BrightPath Cleaning Banner</title>
<link href="https://fonts.googleapis.com/css2?family=Poppins:wght@400;600;700;800&display=swap" rel="stylesheet">
<style>
  :root {
    --white: #ffffff;
    --brand-blue: #15699a;
    --deep-blue: #135d88;
    --teal: #27b3a0;
    --sun: #f3c417;
    --ink: #14233a;
    --navy: #0f2a4a;
  }
  * { margin: 0; padding: 0; box-sizing: border-box; }
  html, body {
    width: 1200px; height: 600px; overflow: hidden;
    background: var(--white);
    font-family: "Poppins", sans-serif;
  }
  .banner { position: relative; width: 1200px; height: 600px; overflow: hidden; background: var(--white); }
  .wave { position: absolute; inset: 0; width: 1200px; height: 600px; }

  .brand {
    position: absolute; left: 40px; top: 118px; width: 250px;
    display: flex; align-items: center; gap: 12px;
  }
  .brand-square { width: 26px; height: 26px; background: var(--teal); flex: none; }
  .brand-name {
    color: var(--teal); font-weight: 600; font-size: 30px; line-height: 1.05;
    letter-spacing: 1px;
  }
  .divider {
    position: absolute; left: 302px; top: 46px; width: 4px; height: 174px;
    background: var(--deep-blue);
  }

  .tagline {
    position: absolute; left: 346px; top: 40px; width: 500px;
    color: var(--ink); font-size: 28px; font-weight: 400; line-height: 36px;
  }
  .call-label {
    position: absolute; left: 346px; top: 110px; height: 34px; padding: 0 10px;
    background: var(--deep-blue); color: var(--white);
    font-size: 22px; line-height: 34px; font-weight: 400;
  }
  .phone {
    position: absolute; left: 344px; top: 148px;
    color: var(--deep-blue); font-size: 68px; line-height: 1; font-weight: 700;
    letter-spacing: -1.5px; white-space: nowrap;
  }

  .services-title {
    position: absolute; left: 78px; top: 330px;
    font-size: 34px; font-weight: 800; color: var(--white); letter-spacing: -0.5px;
  }
  .services-title .accent { color: var(--sun); }

  .service-card {
    position: absolute; top: 384px; width: 208px; height: 182px;
    clip-path: polygon(23px 0, 100% 0, calc(100% - 23px) 100%, 0 100%);
  }
  .service-card.light { background: var(--white); }
  .service-card.bright { background: var(--sun); }
  .service-photo {
    position: absolute; left: 3px; top: 3px; width: 202px; height: 124px;
    clip-path: polygon(22px 0, 100% 0, calc(100% - 16px) 100%, 0 100%);
  }
  .service-label {
    position: absolute; left: 0; right: 0; bottom: 0; height: 55px;
    display: flex; align-items: center; justify-content: center; text-align: center;
    padding-right: 6px;
    color: var(--navy); font-size: 15.5px; font-weight: 800; line-height: 19px;
  }
  .photo-home { background: linear-gradient(160deg, #e9e4de, #b99a7a 60%, #e7703a); }
  .photo-office { background: linear-gradient(160deg, #dfe4e8, #8b8f94 60%, #4d5156); }
  .photo-disinfect { background: linear-gradient(160deg, #f1f2f3, #cfd2d5 60%, #8d9399); }
  .photo-site { background: linear-gradient(160deg, #d9d9d7, #9ea3a8 55%, #2f5fae); }

  .hero-photo {
    position: absolute; left: 812px; top: 0; width: 388px; height: 600px;
    background: linear-gradient(170deg, rgba(255,255,255,0) 0%, #e8c98e 22%, #5b86c4 45%, #2b59a8 70%, #f2d037 85%, #1f3f7a 100%);
    clip-path: polygon(220px 0, 100% 0, 100% 100%, 0 100%, 0 320px);
  }
</style>
</head>
<body>
<div class="banner">
  <svg class="wave" viewBox="0 0 1200 600" aria-hidden="true">
    <path d="M0,268 C200,298 360,330 530,305 C720,278 900,238 1200,238 L1200,600 L0,600 Z" fill="var(--sun)"/>
    <path d="M0,292 C220,338 390,345 550,326 C730,302 910,262 1200,264 L1200,600 L0,600 Z" fill="var(--brand-blue)"/>
  </svg>

  <div class="hero-photo" role="img" aria-label="Smiling cleaner in a checked shirt holding a bucket of cleaning supplies with yellow gloves"></div>

  <div class="brand">
    <span class="brand-square"></span>
    <span class="brand-name">BRIGHTPATH<br>CLEANING</span>
  </div>
  <div class="divider"></div>

  <p class="tagline">Quality driven and reliable to take care of all your cleaning needs!</p>
  <div class="call-label">Call or text us today on</div>
  <div class="phone">(555)014-2739</div>

  <h2 class="services-title">OUR <span class="accent">SERVICES</span></h2>

  <div class="service-card light" style="left:33px">
    <div class="service-photo photo-home" role="img" aria-label="Mopping a home floor beside an orange bucket"></div>
    <div class="service-label">RESIDENTIAL<br>CLEANING</div>
  </div>
  <div class="service-card bright" style="left:209px">
    <div class="service-photo photo-office" role="img" aria-label="Cleaners wiping desks and windows in an office"></div>
    <div class="service-label">COMMERCIAL<br>CLEANING</div>
  </div>
  <div class="service-card light" style="left:385px">
    <div class="service-photo photo-disinfect" role="img" aria-label="Workers in protective suits disinfecting a room"></div>
    <div class="service-label">ANTIVIRAL<br>DISINFECTION</div>
  </div>
  <div class="service-card bright" style="left:561px">
    <div class="service-photo photo-site" role="img" aria-label="Vacuuming dust on a construction site floor"></div>
    <div class="service-label">CONSTRUCTION<br>CLEANING</div>
  </div>
</div>
</body>
</html>
```